Rebranding Website – Brookvale Clinic for Herbal Care (40 Years)

Organization Description:
The Brookvale Clinic for Herbal Care (BCHC / www.bchc-example.nl) has been a trusted address for more than 40 years for people who choose a natural and sustainable approach to their health. We combine experience and history with a modern, professional approach.

Assignment:
Our current website is outdated and no longer reflects who we are today. We are looking for a new web design that aligns with our renewed logo and is both functional and inspiring. The website should have a clear structure, be user-friendly, and convey trust.

What we are looking for in the design:

A modern, fresh look that matches our logo and color palette logo in attachment.

Goal-oriented: simple and intuitive appointment scheduling.

Informative: space for a blog/news section to share knowledge and updates.

A dedicated page for each therapist with photo, expertise, and contact options.

A separate page for each type of therapy, with explanations and benefits.

A clear and visible link to our webshop (separate website).

Clear navigation and an organized menu structure.

Responsive design (desktop, tablet, mobile).

User-friendly CMS so we can manage and expand content ourselves.

Style Preferences:

- Color palette in line with our logo (green and natural tones, complemented by fresh and calm accents).
- Clean, professional design with plenty of white space.
- Accessible, warm, and inviting.

Functionalities:
- Online appointment scheduling or easy contact options.
- Blog/news section.
- Dedicated pages for therapists and therapies.
- Link to webshop.
- Possibility to expand the offer in the future (e.g., videos, downloads, or e-consultations).

What we would like to avoid:
- Pages that are too cluttered or confusing.
- Excessive text without clear structure.
- Stock photos lacking authenticity.

Target Audience:
People who consciously focus on their health, choose a natural approach, and are looking for a professional and reliable center where expertise and personal attention are central.

Additional Information:
The new website should bridge our 40-year history with the future. A place where visitors feel both familiar and inspired – and where they are immediately invited to get in touch, book an appointment, or visit our webshop.

You find our logo and impression in the uploads.

```html
<!DOCTYPE html>
<html lang="en">
<head>
<meta charset="utf-8">
<title>Brookvale Clinic for Herbal Care – Therapies</title>
<link rel="stylesheet" href="https://fonts.googleapis.com/css2?family=Lora:wght@400;600&family=Montserrat:wght@600;700&display=swap">
<style>
  :root {
    --green-dark: #4a5d23;
    --green-lime: #8dc63f;
    --green-lime-light: #a3d94e;
    --text: #4a4a4a;
    --nav-text: #4a4f45;
    --white: #ffffff;
    --band: #f8f8f7;
  }
  * { box-sizing: border-box; margin: 0; padding: 0; }
  html, body { width: 1200px; height: 960px; overflow: hidden; }
  body { background: var(--white); font-family: "Lora", Georgia, serif; color: var(--text); position: relative; }

  .site-header {
    position: absolute; top: 0; left: 0; width: 1200px; height: 81px;
    background: var(--white); box-shadow: 0 2px 12px rgba(0,0,0,0.08); z-index: 2;
  }
  .brand {
    position: absolute; left: 22px; top: 20px; display: flex; align-items: center; gap: 6px;
    font-family: "Montserrat", sans-serif; font-weight: 700; font-size: 15px; color: var(--green-dark);
  }
  .brand-dot { width: 12px; height: 12px; border-radius: 50%; background: var(--green-lime); }
  .main-nav a {
    position: absolute; top: 30px; font-size: 16.5px; color: var(--nav-text); text-decoration: none;
  }
  .main-nav a.active::after {
    content: ""; position: absolute; left: 0; right: 0; top: 26px; height: 2px; background: var(--green-lime);
  }
  .webshop-link {
    position: absolute; left: 876px; top: 30px; font-size: 16.5px; font-weight: 600;
    color: var(--green-dark); text-decoration: none;
  }
  .book-button {
    position: absolute; left: 987px; top: 21px; width: 177px; height: 41px; border-radius: 6px;
    background: linear-gradient(90deg, var(--green-lime), var(--green-lime-light));
    color: var(--white); font-family: "Montserrat", sans-serif; font-weight: 700; font-size: 14.5px;
    display: flex; align-items: center; justify-content: center; text-decoration: none;
    box-shadow: 0 4px 10px rgba(141,198,63,0.35);
  }

  .section-title {
    position: absolute; left: 0; width: 1200px; text-align: center;
    font-family: "Montserrat", sans-serif; font-weight: 700; font-size: 48px; color: var(--green-dark);
  }
  .therapies-title { top: 113px; }

  .therapy-card {
    position: absolute; top: 232px; width: 356px; height: 383px; background: var(--white);
    border-radius: 15px; box-shadow: 0 6px 20px rgba(0,0,0,0.09); text-align: center;
  }
  .therapy-icon {
    position: absolute; left: 131px; top: 30px; width: 94px; height: 94px; border-radius: 50%;
    background: radial-gradient(circle at 40% 35%, var(--green-lime-light), var(--green-lime));
    box-shadow: 0 8px 18px rgba(141,198,63,0.35);
    display: flex; align-items: center; justify-content: center;
  }
  .therapy-name {
    position: absolute; top: 146px; left: 0; width: 100%;
    font-family: "Montserrat", sans-serif; font-weight: 600; font-size: 22.5px; color: var(--green-dark);
  }
  .therapy-text {
    position: absolute; top: 191px; left: 33px; width: 290px;
    font-size: 17.5px; line-height: 27.5px; color: var(--text);
  }
  .learn-more {
    position: absolute; top: 324px; left: 0; width: 100%;
    font-size: 15px; font-weight: 600; color: var(--green-lime); text-decoration: none;
    display: flex; justify-content: center; align-items: center; gap: 8px;
  }

  .testimonials-band {
    position: absolute; left: 0; top: 735px; width: 1200px; height: 225px; background: var(--band);
  }
  .testimonials-title { top: 842px; }
</style>
</head>
<body>
  <header class="site-header">
    <div class="brand"><span class="brand-dot"></span>BCHC</div>
    <nav class="main-nav">
      <a href="#" style="left:222px">Home</a>
      <a href="#" style="left:292px">About Us</a>
      <a href="#" class="active" style="left:387px">Therapies</a>
      <a href="#" style="left:487px">Team</a>
      <a href="#" style="left:555px">Knowledge</a>
      <a href="#" style="left:663px">Contact</a>
    </nav>
    <a href="#" class="webshop-link">Our Webshop</a>
    <a href="#" class="book-button">Book Appointment</a>
  </header>

  <h2 class="section-title therapies-title">Our Core Therapies</h2>

  <article class="therapy-card" style="left:22px">
    <div class="therapy-icon">
      <svg width="38" height="38" viewBox="0 0 24 24" fill="none" stroke="#fff" stroke-width="2" stroke-linejoin="round">
        <rect x="4" y="3" width="8" height="18" rx="2"/>
        <path d="M12 8l3-3 4 4-7 7"/><path d="M12 21h7a1 1 0 0 0 1-1v-5l-3-1"/>
      </svg>
    </div>
    <h3 class="therapy-name">Acupuncture</h3>
    <p class="therapy-text">A traditional healing technique that involves the insertion of fine needles to stimulate specific points on the body.</p>
    <a href="#" class="learn-more">Learn More
      <svg width="18" height="12" viewBox="0 0 18 12" fill="none" stroke="currentColor" stroke-width="1.8"><path d="M1 6h15M11 1l5 5-5 5"/></svg></a>
  </article>

  <article class="therapy-card" style="left:415px">
    <div class="therapy-icon">
      <svg width="38" height="38" viewBox="0 0 24 24" fill="none" stroke="#fff" stroke-width="2" stroke-linejoin="round" stroke-linecap="round">
        <path d="M9 3h6M10 3v6l-5 9a2 2 0 0 0 2 3h10a2 2 0 0 0 2-3l-5-9V3"/><path d="M7 15h10"/>
      </svg>
    </div>
    <h3 class="therapy-name">Homeopathy</h3>
    <p class="therapy-text">A natural form of medicine based on the principle of 'like cures like' to trigger the body's natural healing systems.</p>
    <a href="#" class="learn-more">Learn More
      <svg width="18" height="12" viewBox="0 0 18 12" fill="none" stroke="currentColor" stroke-width="1.8"><path d="M1 6h15M11 1l5 5-5 5"/></svg></a>
  </article>

  <article class="therapy-card" style="left:808px">
    <div class="therapy-icon">
      <svg width="38" height="38" viewBox="0 0 24 24" fill="none" stroke="#fff" stroke-width="2" stroke-linejoin="round" stroke-linecap="round">
        <circle cx="12" cy="12" r="9"/>
        <path d="M4 9l4 1 2 3-2 3 1 4M14 3.5l-1 3 3 2 4-1M15 20l1-4 3-1"/>
      </svg>
    </div>
    <h3 class="therapy-name">Naturopathy</h3>
    <p class="therapy-text">A holistic approach to wellness using natural remedies to help the body heal itself and embrace a healthier lifestyle.</p>
    <a href="#" class="learn-more">Learn More
      <svg width="18" height="12" viewBox="0 0 18 12" fill="none" stroke="currentColor" stroke-width="1.8"><path d="M1 6h15M11 1l5 5-5 5"/></svg></a>
  </article>

  <section class="testimonials-band"></section>
  <h2 class="section-title testimonials-title">What Our Patients Say</h2>
</body>
</html>
```